Tri-fold Brochure, Postcard & Letterhead Design | ||
Small Engineering Consulting & Services Firm for Building Energy Efficiency | ||
I want to have tri-fold brochure and postcard designs that can represent our company well. Our company is providing engineering consulting and services to improve energy efficiency of building mechanical systems and thus reduce energy consumptions of large commercial buildings. The details of the company information can be found in the website: www.corvalith.com, and any questions about the can be routed to tkal@corvalith.com. I have my company logo and biz card design in different format (originally designed by Emblem Craft Hub) and provide them to designers upon request. | ||
Building owners and facility managers of commercial, institutional and industrial buildings, including large office buildings, hospitals, schools and university campuses, data centers, etc. | ||
The tri-fold brochure and postcard should be designed in a way that its contents can be editable in MS Publisher or Word. The letter head can be designed for use in MS Word. |
HVAC_system_solutions_728.jpg Hello, designers! As posted in our website www.corvalith.com, our company is providing services to improve building energy efficiency. Our customers are building owners, facility managers and operators. The real focus of our business is to optimize the operation of building mechanical systems. We don't do the lighting ourselves and typically oursource the lighting portion. In a building, mechanical systems consume more than 50% of energy for heating, ventilating and air-conditioning. So I would like to have images related to the building mechanical systems. You may google images of "HVAC", "chillers", "AHU", and/or "building automation systems". I will upload some samples from google images. I hope it can help. Thanks, |
CORVALITH_23480_FinalLogo_D4L4_714.jpg Use the uploaded logo and also reference the business card design. To understand the company's services and characters, check out the company website at www.corvalith.com |

```html
<!DOCTYPE html>
<html lang="en">
<head>
<meta charset="utf-8">
<title>Corvalith Brochure – Inside Panels</title>
<link href="https://fonts.googleapis.com/css2?family=Arimo:ital,wght@0,400;0,700;1,400;1,700&display=swap" rel="stylesheet">
<style>
  :root {
    --tab-red: #e0452a;
    --tab-dark: #c23218;
    --ink: #222;
    --blue: #1f5fa8;
    --red: #d8321b;
    --green: #2e8b2e;
    --fold: #9aa4ae;
    --paper: #ffffff;
    --photo-grey: #c9ced3;
    --diagram: #eef1f4;
  }
  * { margin: 0; padding: 0; box-sizing: border-box; }
  html, body { width: 1200px; height: 965px; overflow: hidden; background: var(--paper); }
  body { position: relative; font-family: "Arimo", Arial, sans-serif; color: var(--ink); }

  .fold { position: absolute; top: 0; height: 965px; border-left: 2px dashed var(--fold); }
  .panel { position: absolute; top: 0; height: 965px; }
  .panel-services { left: 0; width: 388px; }
  .panel-procedure { left: 398px; width: 390px; }
  .panel-case { left: 796px; width: 404px; }

  .tab {
    position: absolute; top: 18px; left: 10px; right: 10px; height: 40px;
    background: linear-gradient(180deg, var(--tab-red), var(--tab-dark));
    border-radius: 4px;
    color: #fff; font-weight: 700; font-size: 19px; letter-spacing: .5px;
    padding: 9px 0 0 12px;
  }

  .intro {
    position: absolute; top: 72px; left: 30px; width: 345px;
    font-size: 15.5px; line-height: 1.32; text-align: justify;
  }
  .service-list { position: absolute; top: 255px; left: 26px; width: 340px; list-style: none; }
  .service-list li {
    font-style: italic; color: var(--blue); font-size: 16px; line-height: 1.3;
    padding-left: 18px; position: relative; margin-bottom: 18px;
  }
  .service-list li::before {
    content: ""; position: absolute; left: 2px; top: 8px; width: 6px; height: 6px;
    background: var(--blue); border-radius: 50%;
  }
  .chiller-photo {
    position: absolute; left: 0; top: 690px; width: 360px; height: 265px;
    background: radial-gradient(ellipse at 50% 55%, #dde1e5 0%, var(--photo-grey) 60%, #ffffff 100%);
  }

  .phase { position: absolute; left: 22px; width: 360px; }
  .phase h3 { font-size: 17px; font-style: italic; font-weight: 700; margin-bottom: 4px; }
  .phase h3 span { color: var(--red); font-style: normal; font-weight: 400; }
  .phase ol { list-style: none; padding-left: 22px; }
  .phase li { font-style: italic; font-size: 15.5px; line-height: 1.32; }
  .p1 { top: 72px; } .p2 { top: 245px; } .p3 { top: 420px; } .p4 { top: 590px; }
  .bas-diagram {
    position: absolute; left: 30px; top: 765px; width: 340px; height: 195px;
    background: var(--diagram);
  }

  .case-title { position: absolute; top: 72px; left: 28px; color: var(--green); font-size: 17px; font-weight: 700; font-style: italic; }
  .case-note { position: absolute; top: 100px; left: 22px; width: 360px; color: var(--blue); font-size: 16px; line-height: 1.3; }
  .facility { position: absolute; top: 168px; left: 22px; width: 370px; font-size: 15.5px; line-height: 1.3; }
  .facts { position: absolute; top: 228px; left: 22px; list-style: none; width: 375px; }
  .facts li { font-style: italic; font-size: 12.5px; line-height: 1.55; padding-left: 18px; position: relative; }
  .facts li::before { content: ""; position: absolute; left: 2px; top: 6px; width: 7px; height: 7px; background: var(--green); }
  .chart { position: absolute; left: 72px; }
  .chart-top { top: 525px; }
  .chart-bottom { top: 715px; }
</style>
</head>
<body>

<div class="fold" style="left:392px"></div>
<div class="fold" style="left:791px"></div>

<section class="panel panel-services">
  <div class="tab">SERVICES</div>
  <p class="intro">CORVALITH's highly educated and experienced staff can provide any and all of the following services with special attention to the type of facility. The uniqueness of each facility type requires the correct expertise to meet both thermal comfort requirements and the need for energy efficiency.</p>
  <ul class="service-list">
    <li>HVAC Engineering Consulting</li>
    <li>Investment-Grade Energy Audits</li>
    <li>New Building Commissioning and Re-Commissioning</li>
    <li>Building Retrofits and Integrated Energy System Commissioning and Optimization (BRISCO)</li>
    <li>EcoRate Certification</li>
    <li>Measurement and Verification (M&amp;V)</li>
    <li>Training and Documentation</li>
  </ul>
  <div class="chiller-photo" role="img" aria-label="Photograph of an air-cooled chiller unit"></div>
</section>

<section class="panel panel-procedure">
  <div class="tab">PROCEDURE</div>
  <div class="phase p1">
    <h3>Phase 1: <span>PRELIMINARY STUDIES</span></h3>
    <ol>
      <li>1. Compare and analyze energy use index by building types</li>
      <li>2. Use EcoRate, NEBRA Standard 90.1</li>
      <li>3. Preliminary work-through.</li>
      <li>4. Evaluate economic values of the projects.</li>
    </ol>
  </div>
  <div class="phase p2">
    <h3>Phase 2: <span>ENERGY AUDITS</span></h3>
    <ol>
      <li>1. Collect and analyze existing documents.</li>
      <li>2. Interview with site staffs.</li>
      <li>3. On-site evaluation for 2~5 days</li>
      <li>4. Calculate energy savings</li>
      <li>5. Provide audit reports and proposals</li>
    </ol>
  </div>
  <div class="phase p3">
    <h3>Phase 3: <span>IMPLEMENTATION</span></h3>
    <ol>
      <li>1. Kick-off meeting with onsite staff's approval</li>
      <li>2. Retrofit specs, bids, installations.</li>
      <li>3. Functional tests for new equipment</li>
      <li>4. Optimization and custom algorithm</li>
      <li>5. End-of-work report</li>
    </ol>
  </div>
  <div class="phase p4">
    <h3>Phase 4: <span>M&amp;V</span></h3>
    <ol>
      <li>1. Immediate checks for results</li>
      <li>2. Seasonal check-ups</li>
      <li>3. Long-term M&amp;V for building energy usage</li>
      <li>4. Final report</li>
      <li>5. Case studies and benchmarking</li>
    </ol>
  </div>
  <div class="bas-diagram" role="img" aria-label="Technical schematic of a building automation system network"></div>
</section>

<section class="panel panel-case">
  <div class="tab">CASE STUDY</div>
  <p class="case-title">Case Study 1</p>
  <p class="case-note">(The case studies listed below were summaries of Dr. Kal's engineering performance during his career.)</p>
  <p class="facility">Facility: A semiconductor technology company in Dallas, Texas</p>
  <ul class="facts">
    <li>A campus of 8 buildings with offices and labs</li>
    <li>1,200,000 square feet total</li>
    <li>97 Single Duct VAV AHU and 35 Single Zone AHU</li>
    <li>2,255 VAV terminal boxes and 57 fan powered boxes</li>
    <li>Chilled water is supplied by an on-campus central plant</li>
    <li>4 chillers: 2 chillers @1200 ton, 2 chillers @900 ton</li>
    <li>2.7 million gallon thermal storage tank (chilled water)</li>
  </ul>

  <svg class="chart chart-top" width="320" height="180" viewBox="0 0 320 180">
    <text x="170" y="12" font-size="8" text-anchor="middle" font-family="Arimo, sans-serif">Chilled Water Plant kW</text>
    <rect x="30" y="20" width="280" height="140" fill="none" stroke="#999" stroke-width="1"/>
    <g stroke="#ddd" stroke-width="1">
      <line x1="30" y1="48" x2="310" y2="48"/><line x1="30" y1="76" x2="310" y2="76"/>
      <line x1="30" y1="104" x2="310" y2="104"/><line x1="30" y1="132" x2="310" y2="132"/>
    </g>
    <polyline fill="none" stroke="#7a7a7a" stroke-width="1.5"
      points="40,52 62,60 84,48 106,58 128,55 150,66 172,50 194,62 216,54 238,60 260,50 282,58 300,52"/>
    <g fill="#7a7a7a">
      <circle cx="40" cy="52" r="2"/><circle cx="84" cy="48" r="2"/><circle cx="128" cy="55" r="2"/>
      <circle cx="172" cy="50" r="2"/><circle cx="216" cy="54" r="2"/><circle cx="260" cy="50" r="2"/><circle cx="300" cy="52" r="2"/>
    </g>
    <polyline fill="none" stroke="#555" stroke-width="1.5"
      points="40,118 62,122 84,116 106,124 128,120 150,126 172,118 194,122 216,116 238,124 260,120 282,118 300,122"/>
  </svg>

  <svg class="chart chart-bottom" width="320" height="245" viewBox="0 0 320 245">
    <text x="170" y="12" font-size="8" text-anchor="middle" font-family="Arimo, sans-serif">Daily Load Profile</text>
    <g font-size="7" font-family="Arimo, sans-serif">
      <line x1="110" y1="22" x2="124" y2="22" stroke="#d8321b" stroke-width="2"/><text x="128" y="25">Before</text>
      <line x1="190" y1="22" x2="204" y2="22" stroke="#2e8b2e" stroke-width="2"/><text x="208" y="25">After</text>
    </g>
    <rect x="30" y="32" width="280" height="195" fill="none" stroke="#999" stroke-width="1"/>
    <g stroke="#e3e3e3" stroke-width="1">
      <line x1="30" y1="71" x2="310" y2="71"/><line x1="30" y1="110" x2="310" y2="110"/>
      <line x1="30" y1="149" x2="310" y2="149"/><line x1="30" y1="188" x2="310" y2="188"/>
    </g>
    <polyline fill="none" stroke="#d8321b" stroke-width="1.5"
      points="32,150 50,145 70,140 90,120 110,75 130,68 150,66 170,70 190,72 210,68 225,70 232,150 250,165 270,170 290,175 308,178"/>
    <polyline fill="none" stroke="#2e8b2e" stroke-width="1.5"
      points="32,190 50,188 70,185 90,170 110,150 130,144 150,140 170,145 190,148 210,142 230,150 250,180 270,195 290,198 308,200"/>
  </svg>
</section>

</body>
</html>
```